Tarn - Stationary Design/Layout

We are a well established clothing design and manufacturing company (Tarn Sourcing) based in London UK, with our own factory in Bangladesh, supplying to many fashion retailers and brands. Our factory has very high environmental and ethical standards with people at its heart. Our quality of garments are second to none.
Our new logo has been proudly developed by the Pixel Guild community last month, we are now in the second phase and need the layout designed for our letterheads, double sided business cards, compliment slip and clothing ticket. Feel as creative as you like, but make sure it looks great!!
***The Logo - the logo design and colour is set and should NOT be changed and stay on a dark grey backround. The logo artwork to use is attached.
***Details to use for the business card:
Dorian Pelham
Direct Line: 020 7946 0158
dorian@tarnsourcing-example.com
Tarn Sourching Ltd.
57 - 59 Hollin Row
Corvale . Ashmere
NW9 4QT
Switchboard: 020 7946 0274
Fax: 020 7946 0274
www.tarnsourcing-example.co.uk
***Details to use for the letterhead and compliment slip:
Tarn Sourching Ltd.
57 - 59 Hollin Row
Corvale . Ashmere
NW9 4QT
Fax: 020 7946 0274
www.tarnsourcing-example.co.uk
***Details for Swing Ticket:
Size: 12cm height by 5.5cm width
One side need to have just the logo without the 'Sourcing', on the other it needs to stay blank

```html
<!DOCTYPE html>
<html lang="en">
<head>
<meta charset="utf-8">
<title>Tarn Sourcing – Letterhead</title>
<link href="https://fonts.googleapis.com/css2?family=Questrial&family=Noticia+Text&display=swap" rel="stylesheet">
<style>
  :root {
    --backdrop: #a6a7aa;
    --paper: #ffffff;
    --charcoal: #3c3c3d;
    --aqua: #abdde1;
    --header-grey: #b9b9b9;
    --ink: #1f1f1f;
    --footer-ink: #3a3a3a;
  }
  html, body {
    margin: 0;
    padding: 0;
    width: 968px;
    height: 1200px;
    overflow: hidden;
    background: var(--backdrop);
  }
  .letterhead {
    position: absolute;
    left: 44px;
    top: 30px;
    width: 1036px;
    height: 1342px;
    background: var(--paper);
    transform: scale(0.85);
    transform-origin: 0 0;
    overflow: hidden;
  }
  .header-band, .footer-band {
    position: absolute;
    left: 0;
    width: 1036px;
  }
  .header-band { top: 0; height: 170px; }
  .footer-band { bottom: 0; height: 100px; }

  .brand-name {
    position: absolute;
    left: 72px;
    top: 46px;
    margin: 0;
    font-family: "Questrial", sans-serif;
    font-size: 30px;
    font-weight: 400;
    letter-spacing: 1px;
    color: var(--aqua);
  }
  .company-address, .company-contact {
    position: absolute;
    top: 28px;
    margin: 0;
    font-family: "Questrial", sans-serif;
    font-size: 13px;
    line-height: 17px;
    color: var(--header-grey);
    font-style: normal;
    white-space: nowrap;
  }
  .company-address { left: 640px; }
  .company-contact { left: 784px; }
  .company-address .company-title { color: var(--aqua); }
  .company-contact .label { color: #ffffff; }

  .letter-body {
    position: absolute;
    left: 183px;
    top: 240px;
    width: 790px;
    font-family: "Noticia Text", serif;
    font-size: 12.6px;
    letter-spacing: -0.25px;
    line-height: 20.3px;
    color: var(--ink);
    white-space: nowrap;
  }
  .letter-body p { margin: 0 0 20.3px 0; }
  .letter-body .sign-off { margin-top: 40.6px; margin-bottom: 60.9px; }

  .footer-url {
    position: absolute;
    left: 0;
    width: 1036px;
    top: 1297px;
    margin: 0;
    text-align: center;
    font-family: "Questrial", sans-serif;
    font-size: 12.5px;
    letter-spacing: 0.3px;
    color: var(--footer-ink);
    font-weight: 700;
  }
</style>
</head>
<body>
<main class="letterhead">
  <svg class="header-band" viewBox="0 0 1036 170" aria-hidden="true">
    <path d="M0 143 C 160 132, 260 116, 420 118 C 600 120, 700 160, 880 160 C 960 160, 1000 153, 1036 145 L1036 0 L0 0 Z" fill="var(--charcoal)"/>
    <path d="M255 104 C 330 100, 380 100, 440 102 C 600 108, 700 142, 880 142 C 950 142, 1000 136, 1036 130" fill="none" stroke="#8a8a8b" stroke-width="1" stroke-dasharray="12 9"/>
  </svg>

  <h1 class="brand-name">TARN SOURCING</h1>

  <address class="company-address">
    <span class="company-title">Tarn Sourching Ltd.</span><br>
    57 - 59 Hollin Row<br>
    Corvale . Ashmere<br>
    NW9 4QT
  </address>
  <p class="company-contact">
    <span class="label">switchboard:</span> (020) 7946 0274<br>
    <span class="label">f:</span> (020) 7946 0274<br>
    <span class="label">w:</span> www.tarnsourcing-example.co.uk
  </p>

  <section class="letter-body">
    <p>May 13th 2011</p>
    <p>Recipient’s name<br>Adress<br>City, State, Zip code</p>
    <p>Dear Recipient</p>
    <p>Lorem ipsum dolor sit amet, gravida vitae elementum aptent vel dis tristique, eros et curabitur massa ligula, erat sodales pede,<br>
    integer sed, elementum viverra facilisis vitae. Euismod etiam, non viverra pulvinar tortor in. Ut venenatis purus eu nam eros,<br>
    viverra dui, imperdiet eu. Elit risus dui luctus. Nec quis quam, arcu et mauris hendrerit consequatur. Feugiat donec ad tincidunt.<br>
    Fringilla tempor, sapien hendrerit varius sed nulla velit ut, id est euismod velit diam luctus semper. Amet condimentum.<br>
    Eu sollicitudin, pellentesque consectetuer et, netus vel ut nulla.</p>
    <p>Libero ornare aliquet. Scelerisque odio venenatis, quam amet. Wisi egestas volutpat neque turpis duis, egestas felis eu aliquam<br>
    sodales ac sem, elit nulla eget sed quam sit ante, torquent erat maecenas porttitor ac, dui mi vitae pede augue. Dignissim ultrices<br>
    suspendisse, auctor suscipit est ipsum. Sollicitudin erat viverra eleifend, sed ut aliquam vitae cum viverra.</p>
    <p>Pulvinar mollis urna velit leo mi rutrum, neque pretium sed aliquam mi aute faucibus, quis magna blandit nec velit, in aenean<br>
    leo dictumst malesuada. Libero suscipit ultrices turpis aliquet suspendisse justo, aptent felis nec mauris pede amet vitae, nunc<br>
    rutrum class libero fringilla risus vivamus. Mi maecenas sit tempus nec nam ipsum, condimentum quis sed ligula purus tempor<br>
    est, mi ridiculus non mi. Malesuada fermentum posuere senectus, id blandit mus eleifend tellus, natoque mi nulla felis lorem<br>
    dolor venenatis, mi vehicula vitae nec in vestibulum nec. Iaculis nec, integer justo pellentesque turpis pretium turpis montes.<br>
    Et commodo ut. Ante cursus justo. Nostra quam, praesent purus quis est bibendum. Lorem ipsum magna pellentesque in.<br>
    Vitae ut sollicitudin tincidunt consectetuer lorem, elit donec lectus pellentesque pellentesque ac eu, tristique fringilla, duis<br>
    facilisis faucibus risus eget pellentesque, curabitur eu sit porttitor aliquam occaecat felis.</p>
    <p>Purus morbi, sed integer molestie metus ea quam, morbi adipiscing posuere dapibus accumsan euismod et. Posuere et turpis<br>
    porta libero, habitant neque dapibus curabitur, lorem condimentum quis sit eget convallis. Aliquam mauris qui faucibus nullam,<br>
    libero sit mi mi. In quisque nullam per, rutrum nec sed magnis magna, luctus ante suspendisse. In fugit gravida scelerisque in<br>
    dui et, earum elementum tempus nunc elementum neque in, donec fermentum sem. At pede feugiat euismod, vel venenatis<br>
    leo integer pellentesque. Sit feugiat varius, montes at dolor ut egestas metus, auctor massa euismod dapibus, tellus ultricies<br>
    suspendisse proin morbi erat anim, in orci luctus.</p>
    <p class="sign-off">Yours Sincerely</p>
    <p>Dorian Pelham<br>CEO</p>
  </section>

  <svg class="footer-band" viewBox="0 0 1036 100" aria-hidden="true">
    <path d="M0 30 C 120 16, 230 8, 340 8 C 520 8, 700 24, 860 28 C 950 30, 1000 26, 1036 22 L1036 100 L0 100 Z" fill="var(--aqua)"/>
  </svg>
  <p class="footer-url">www.tarnsourcing-example.co.uk</p>
</main>
</body>
</html>
```